Simple and Clean business card design

We would like the design to be simple clean and to incorporate our colors.

We are open to your design and talent, we have the dots in our logo as we think of it as data points and we connect data points for people.

We are open to see the great creative and clean design you bring to the table

Contact Information for Business Card

please include: name, position, email, phone and website

Font styles to use
Sans Serif

Requirements
Must have
• my colors incorporated, simplicity
Nice to have
• lots of white space, simplicity
Should not have
• complexicity/ complex art

```html
<!DOCTYPE html>
<html lang="en">
<head>
<meta charset="utf-8">
<title>Tolvana business card</title>
<link rel="stylesheet" href="https://fonts.googleapis.com/css2?family=Questrial&display=swap">
<style>
  :root {
    --stage: #5c5c5c;
    --card-dark: #000000;
    --card-light: #ffffff;
    --ink: #222222;
    --ink-light: #ffffff;
    --accent-blue: #4285f4;
  }
  * { margin: 0; padding: 0; box-sizing: border-box; }
  html, body {
    width: 1199px;
    height: 1200px;
    overflow: hidden;
    background: var(--stage);
    font-family: "Questrial", sans-serif;
  }
  .canvas {
    position: relative;
    width: 1199px;
    height: 1200px;
  }
  .card {
    position: absolute;
    top: 182px;
    width: 479px;
    height: 836px;
    border-radius: 26px;
  }
  .card--back {
    left: 98px;
    background: var(--card-dark);
  }
  .card--front {
    left: 622px;
    background: var(--card-light);
    color: var(--ink);
    text-align: center;
  }
  .back-wordmark {
    position: absolute;
    left: 0;
    right: 0;
    top: 374px;
    display: flex;
    align-items: center;
    justify-content: center;
    gap: 16px;
    color: var(--ink-light);
    font-size: 58px;
    line-height: 1;
    letter-spacing: 1px;
  }
  .back-wordmark .dot {
    width: 26px;
    height: 26px;
    border-radius: 50%;
    background: var(--accent-blue);
  }
  .wordmark {
    position: absolute;
    left: 0;
    right: 0;
    top: 296px;
    top: 114px;
    font-size: 84px;
    line-height: 1;
    letter-spacing: 3px;
    color: var(--ink);
  }
  .person {
    position: absolute;
    left: 0;
    right: 0;
    top: 578px;
  }
  .person-name {
    font-size: 35px;
    line-height: 1;
    letter-spacing: 1px;
  }
  .person-role {
    font-size: 25px;
    line-height: 1;
    margin-top: 0;
  }
  .contact {
    position: absolute;
    left: 0;
    right: 0;
    top: 694px;
    list-style: none;
    font-size: 26px;
    line-height: 38px;
  }
</style>
</head>
<body>
<main class="canvas">
  <section class="card card--back" aria-label="Card back">
    <div class="back-wordmark"><span class="dot"></span><span>Tolvana</span></div>
  </section>

  <section class="card card--front" aria-label="Card front">
    <div class="wordmark">Tolvana</div>
    <div class="person">
      <p class="person-name">JOHN DOE</p>
      <p class="person-role">owner</p>
    </div>
    <ul class="contact">
      <li>e&nbsp; : hello@tolvanamail.co</li>
      <li>p&nbsp; : 0198 765 432</li>
      <li>w : www.tolvana.co</li>
    </ul>
  </section>
</main>
</body>
</html>
```